CFO services graphic design

I own a business consulting firm called Marlowe Consulting and we need a graphic for CFO services in our colours and branding. The attached file "CFO services to be put into Marlowe consulting theme", shows the content for the design. The two other files show the theme and colours for the new design.

```html
<!DOCTYPE html>
<html lang="en">
<head>
<meta charset="utf-8">
<title>Marlowe Consulting – CFO Services</title>
<link rel="stylesheet" href="https://fonts.googleapis.com/css2?family=Barlow+Condensed:wght@500;600;700&display=swap">
<style>
  :root {
    --page-bg: #ffffff;
    --ring-orange: #f7941d;
    --wheel-rim: #e6e6e7;
    --hub-bg: #e6e6e7;
    --petal-light: #23a9e1;
    --petal-dark: #0b3a87;
    --petal-mid: #164fba;
    --core-navy: #012352;
    --arrow-navy: #0b2a55;
    --label-white: #ffffff;
  }
  html, body {
    margin: 0;
    padding: 0;
    width: 1200px;
    height: 956px;
    overflow: hidden;
    background: var(--page-bg);
  }
  .cfo-wheel {
    display: block;
    width: 1200px;
    height: 956px;
  }
  .outer-ring {
    fill: none;
    stroke: var(--ring-orange);
    stroke-width: 20;
    stroke-dasharray: 226.36 12;
    stroke-dashoffset: 232.36;
  }
  .wheel-rim { fill: var(--wheel-rim); }
  .petal { stroke: var(--wheel-rim); stroke-width: 8; stroke-linejoin: round; }
  .petal--light { fill: var(--petal-light); }
  .petal--dark { fill: var(--petal-dark); }
  .petal--mid { fill: var(--petal-mid); }
  .core { fill: var(--core-navy); }
  .arrow-shaft { stroke: var(--arrow-navy); stroke-width: 5; }
  .arrow-head { fill: var(--arrow-navy); }
  .label {
    font-family: "Barlow Condensed", sans-serif;
    font-weight: 500;
    font-size: 50px;
    fill: var(--label-white);
    text-anchor: middle;
    letter-spacing: -0.5px;
  }
  .label--strong { font-weight: 700; }
  .label--small { font-size: 27px; font-weight: 500; }
  .core-title {
    font-family: "Barlow Condensed", sans-serif;
    font-weight: 700;
    font-size: 62px;
    fill: var(--label-white);
    text-anchor: middle;
  }
</style>
</head>
<body>
<svg class="cfo-wheel" viewBox="0 0 2000 1594" xmlns="http://www.w3.org/2000/svg" role="img" aria-label="Marlowe Consulting CFO services wheel">
  <defs>
    <path id="petal-shape" d="M -221,-534 A 578 578 0 0 1 221,-534 L 133.2,-321.5 A 143 143 0 0 1 -133.2,-321.5 Z"/>
    <g id="arrow">
      <line class="arrow-shaft" x1="0" y1="-152" x2="0" y2="-185"/>
      <polygon class="arrow-head" points="0,-222 -12,-180 12,-180"/>
    </g>
  </defs>

  <g transform="translate(1000 797)">
    <circle class="outer-ring" r="607" transform="rotate(-90)"/>
    <circle class="wheel-rim" r="584"/>

    <use href="#petal-shape" class="petal petal--light"/>
    <use href="#petal-shape" class="petal petal--dark" transform="rotate(45)"/>
    <use href="#petal-shape" class="petal petal--light" transform="rotate(90)"/>
    <use href="#petal-shape" class="petal petal--mid" transform="rotate(135)"/>
    <use href="#petal-shape" class="petal petal--light" transform="rotate(180)"/>
    <use href="#petal-shape" class="petal petal--dark" transform="rotate(225)"/>
    <use href="#petal-shape" class="petal petal--light" transform="rotate(270)"/>
    <use href="#petal-shape" class="petal petal--mid" transform="rotate(315)"/>

    <use href="#arrow"/>
    <use href="#arrow" transform="rotate(45)"/>
    <use href="#arrow" transform="rotate(90)"/>
    <use href="#arrow" transform="rotate(135)"/>
    <use href="#arrow" transform="rotate(180)"/>
    <use href="#arrow" transform="rotate(225)"/>
    <use href="#arrow" transform="rotate(270)"/>
    <use href="#arrow" transform="rotate(315)"/>

    <circle class="core" r="140"/>
  </g>

  <text class="core-title">
    <tspan x="1000" y="759">CHIEF</tspan>
    <tspan x="1000" y="817">FINANCIAL</tspan>
    <tspan x="1000" y="875">OFFICER</tspan>
  </text>

  <text class="label">
    <tspan x="1000" y="315">COST</tspan>
    <tspan x="1000" y="363">ACCOUNTING &amp;</tspan>
    <tspan x="1000" y="412">COST</tspan>
    <tspan x="1000" y="461">MANAGEMENT</tspan>
  </text>

  <text class="label">
    <tspan x="1290" y="447">CAPITAL</tspan>
    <tspan x="1290" y="496">STRUCTURE</tspan>
    <tspan x="1290" y="545">AND THE COST</tspan>
    <tspan x="1290" y="594">OF CAPITAL</tspan>
  </text>

  <text class="label">
    <tspan x="1430" y="737">LONG-TERM &amp;</tspan>
    <tspan x="1430" y="786">SHORT-TERM</tspan>
    <tspan x="1430" y="835">INVESTMENT</tspan>
    <tspan x="1430" y="884">DECISIONS</tspan>
  </text>

  <text class="label">
    <tspan x="1310" y="1063">PERFORMANCE</tspan>
    <tspan x="1310" y="1111">EVALUATION</tspan>
  </text>

  <text class="label">
    <tspan x="997" y="1188">BUDGETING &amp;</tspan>
    <tspan x="997" y="1236">STRATEGIC</tspan>
    <tspan x="997" y="1285">PLANNING</tspan>
  </text>

  <text class="label">
    <tspan x="685" y="1063">RISK</tspan>
    <tspan x="685" y="1111">MANAGEMENT</tspan>
  </text>

  <text class="label">
    <tspan class="label--strong" x="578" y="770">COMPLIANCE:</tspan>
    <tspan x="578" y="822">TAX, LEGAL AND</tspan>
    <tspan x="578" y="870">REGULATORY</tspan>
  </text>

  <text class="label">
    <tspan class="label--strong" x="688" y="492">COMMUNICATION</tspan>
    <tspan class="label--small" x="688" y="526">BOARD OF DIRECTORS,</tspan>
    <tspan class="label--small" x="688" y="555">CREDITORS, OWNERS, INVESTORS,</tspan>
    <tspan class="label--small" x="688" y="584">CREDIT RATING AGENCIES</tspan>
  </text>
</svg>
</body>
</html>
```